New Wedding Decor Web Design Project - GUARANTEED PAYMENT

We need to have a business website for a brand new wedding decor & events company, Lirovel. We have just established our logo and would love to use this logo on the website.

Because this is a new business venture, we do not have too many pictures to post online. It'd be exciting what your creativity can bring us!

Our website is: www.Lirovel.ca

Target Market(s)

Our clientele demographic is targeted to brides and bridesmaids in their 20-30 years old.

Industry/Entity Type

Wedding

Requirements
Must have
• - Professional, elegant and artistic look
- Modern feeling
- Very catchy flash intro page
- Ability to show Chatterleaf posts
Nice to have
• - Easy to navigate, crisp and clean
- Live pingvox messaging or online messaging

I would like to have navigation pages like: Lirovel Brand, Collections, Features, Contact Us, etc.

Each page I want it to be clean and easy to read. Something like the following website: http://www.brenquavi.com/

We offer:
BACKDROPS
HEAD, CAKE & RECEIVING TABLES DECOR
CHAIRCOVERS
TABLE CLOTHS & OVERLAYS
NAPKINS
CENTREPIECES
CEREMONY SET-UP
CANDELABRA
CRYSTAL GLOBES
LED LIGHTING
CUSTOM DESIGN AISLE RUNNERS
CAKE STANDS
MONEY BOX
CHARGERS
GOBO LIGHTING
Should not have
• - traditional, old style website
- very static (dull)
- too many images or busy layout
- no "standardized" website templates such as: www.zintep.com/gallery/weddings

```html
<!DOCTYPE html>
<html lang="en">
<head>
<meta charset="utf-8">
<title>Lirovel — wedding events</title>
<link rel="stylesheet" href="https://fonts.googleapis.com/css2?family=Didact+Gothic&family=Lato:ital,wght@0,400;0,700;1,400&display=swap">
<style>
:root{
  --page:#eeeeee;
  --paper:#ffffff;
  --ink:#5e5e5e;
  --ink-soft:#8a8a8a;
  --green:#b6d46b;
  --green-deep:#8ab52a;
  --green-ribbon:#9cc234;
  --pink:#f07eae;
  --pink-deep:#d95d92;
  --footer:#878787;
  --footer-dark:#5c5c5c;
  --field:#a9a9a9;
  --lime-text:#cbe27f;
}
*{margin:0;padding:0;box-sizing:border-box}
html,body{width:1062px;height:1200px;overflow:hidden}
body{position:relative;background:var(--page);font-family:"Lato",sans-serif;color:var(--ink)}
.abs{position:absolute}
.heading{font-family:"Didact Gothic",sans-serif;font-weight:400}

/* header */
.ribbon{left:204px;top:78px;width:654px;height:42px}
.logo-card{left:427px;top:0;width:208px;height:128px;background:var(--paper);box-shadow:0 0 18px rgba(0,0,0,.06);border-bottom:2px solid #9a9a9a}
.logo-bloom{left:76px;top:20px;width:58px;height:52px;border-radius:50%;background:radial-gradient(circle at 45% 45%,#f56fa9,#d92f78)}
.logo-name{left:0;width:208px;top:72px;text-align:center;font-family:"Didact Gothic",sans-serif;font-size:34px;color:#7a7a7a;line-height:1}
.logo-tag{right:26px;top:105px;font-family:"Didact Gothic",sans-serif;font-size:11px;color:#9a9a9a}

.nav{left:202px;top:137px;width:658px;height:44px;background:var(--paper);border-top:1px dashed #d8d8d8}
.nav a{position:absolute;top:14px;transform:translateX(-50%);font-family:"Didact Gothic",sans-serif;font-size:13.5px;color:#666;text-decoration:none;white-space:nowrap}

.hero{left:202px;top:181px;height:226px;border-top:1px dashed #ddd}
.photo{position:absolute;top:0;height:100%}

/* services band */
.band-zig{left:0;top:432px;width:1062px;height:9px}
.services{left:0;top:440px;width:1062px;height:188px;background:var(--green)}
.section-title{left:0;width:1062px;text-align:center;font-size:25px;color:#707070}
.service{position:absolute;top:50px;width:88px;height:88px;border-radius:50%;border:4px solid #fff;box-shadow:0 1px 4px rgba(0,0,0,.25);transform:translateX(-50%);overflow:hidden}
.service span{position:absolute;left:0;right:0;top:53px;text-align:center;font-family:"Didact Gothic",sans-serif;font-size:10px;color:#555}
.arrow{position:absolute;top:78px;width:28px;height:36px}
.btn-pink{background:var(--pink);color:#fff;border-radius:4px;box-shadow:0 2px 0 var(--pink-deep);font-family:"Didact Gothic",sans-serif;font-size:16px;text-align:center;line-height:29px;width:92px;height:29px}
.dash{height:0;border-top:1px dashed}

/* collections */
.collection{position:absolute;top:702px;height:125px;width:162px}

/* footer */
.footer-zig{left:0;top:912px;width:1062px;height:9px}
.footer{left:0;top:920px;width:1062px;height:236px;background:var(--footer)}
.footer-title{font-size:23px;color:var(--lime-text)}
.label{font-style:italic;font-size:12px;color:var(--lime-text)}
.field{background:var(--field);border:1px solid #9a9a9a;border-radius:3px;box-shadow:inset 0 1px 2px rgba(0,0,0,.15)}
.social-card{left:201px;top:982px;width:147px;font-size:9px;color:#fff}
.friend{position:absolute;top:60px;width:33px;height:33px;background:linear-gradient(#d8d8d8,#9c9c9c)}
.friend-name{position:absolute;top:96px;width:40px;font-size:6.5px;text-align:center;color:#eee}
.send{left:540px;top:1095px;width:162px;height:23px;background:var(--green-deep);border-radius:4px;color:#fff;font-family:"Didact Gothic",sans-serif;font-size:14px;text-align:center;line-height:23px}
.call-box{left:731px;top:1002px;width:127px;height:111px;background:#9a9a9a;border-radius:3px}
.call-btn{left:15px;top:25px;width:99px;height:37px;border-radius:4px;background:linear-gradient(#5cc4f2,#1f8fd0);color:#fff;font-family:"Didact Gothic",sans-serif;font-size:17px;line-height:37px;padding-left:40px;box-shadow:0 2px 2px rgba(0,0,0,.25)}
.call-icon{left:6px;top:10px;width:36px;height:36px;border-radius:50%;background:var(--green-deep);border:2px solid #fff}
.bottom-bar{left:0;top:1156px;width:1062px;height:44px;background:var(--footer-dark);font-size:10px;color:#fff}
.bottom-bar .links{position:absolute;right:263px;top:15px;word-spacing:4px}
.icon-square{position:absolute;top:11px;width:20px;height:20px;border-radius:3px;background:#3f6fb5}
</style>
</head>
<body>

<!-- header -->
<svg class="abs ribbon" viewBox="0 0 654 42" aria-hidden="true">
  <path d="M0 10 L52 10 L52 30 L0 30 L10 20 Z" fill="#8ab52a"/>
  <path d="M654 10 L602 10 L602 30 L654 30 L644 20 Z" fill="#8ab52a"/>
  <rect x="48" y="2" width="180" height="30" fill="var(--green-ribbon)"/>
  <rect x="426" y="2" width="180" height="30" fill="var(--green-ribbon)"/>
  <path d="M48 32 L60 40 L60 32 Z M606 32 L594 40 L594 32 Z" fill="#6f9120"/>
  <line x1="52" y1="6" x2="228" y2="6" stroke="#c8e07e" stroke-dasharray="3 3"/>
  <line x1="426" y1="6" x2="602" y2="6" stroke="#c8e07e" stroke-dasharray="3 3"/>
</svg>
<div class="abs logo-card">
  <div class="abs logo-bloom" role="img" aria-label="Pink peony flower"></div>
  <div class="abs logo-name">Lirovel</div>
  <div class="abs logo-tag">wedding events</div>
</div>

<nav class="abs nav">
  <a style="left:67px">HOME</a>
  <a style="left:192px">LIROVEL BRAND</a>
  <a style="left:338px">COLLECTIONS</a>
  <a style="left:456px">FEATURES</a>
  <a style="left:572px">CONTACT US</a>
</nav>

<div class="abs hero" style="width:658px">
  <div class="photo" style="left:0;width:208px;background:linear-gradient(160deg,#e8e2ff,#9d8ee0 55%,#5c4f9c)" role="img" aria-label="Draped backdrop with cocktail tables in lilac light"></div>
  <div class="photo" style="left:208px;width:230px;background:linear-gradient(180deg,#f3eef0,#d9cfe0 50%,#b8a8a0)" role="img" aria-label="Reception hall with chandelier and white table settings"></div>
  <div class="photo" style="left:438px;width:220px;background:linear-gradient(200deg,#f6f7ff,#cfd6ee 50%,#e6e8b8)" role="img" aria-label="Head table with sheer drapes and sash"></div>
</div>
<svg class="abs" style="left:190px;top:372px;width:682px;height:48px" aria-hidden="true">
  <path d="M12 0 L12 35 L0 20 Z" fill="#d8d8d8"/>
  <path d="M670 0 L670 35 L682 20 Z" fill="#d8d8d8"/>
</svg>

<!-- services -->
<svg class="abs band-zig" viewBox="0 0 1062 9" preserveAspectRatio="none" aria-hidden="true">
  <defs><pattern id="zigGreen" width="10" height="9" patternUnits="userSpaceOnUse"><path d="M0 9 L5 0 L10 9 Z" fill="var(--green)"/></pattern></defs>
  <rect width="1062" height="9" fill="url(#zigGreen)"/>
</svg>
<section class="abs services">
  <h2 class="abs heading section-title" style="top:14px">our services include</h2>
  <svg class="arrow" style="left:170px" viewBox="0 0 28 36" aria-hidden="true"><path d="M26 2 L6 18 L26 34" fill="none" stroke="var(--pink)" stroke-width="7"/></svg>
  <div class="service" style="left:249px;background:radial-gradient(#fbf2f7,#e6cfe0)" role="img" aria-label="Backdrops"><span>BACKDROPS</span></div>
  <div class="service" style="left:342px;background:radial-gradient(#fff3f6,#ead3dc)" role="img" aria-label="Decor"><span>DECOR</span></div>
  <div class="service" style="left:435px;background:radial-gradient(#fbefe9,#e6cfc6)" role="img" aria-label="Covers"><span>COVERS</span></div>
  <div class="service" style="left:529px;background:radial-gradient(#f8f8f8,#d8d8dc)" role="img" aria-label="Napkins"><span>NAPKINS</span></div>
  <div class="service" style="left:625px;background:radial-gradient(#f7efe6,#d7c6b2)" role="img" aria-label="Centerpieces"><span>CENTERPIECES</span></div>
  <div class="service" style="left:719px;background:radial-gradient(#f8f8f8,#d6d6d6)" role="img" aria-label="Set up"><span>SET UP</span></div>
  <div class="service" style="left:814px;background:radial-gradient(#fbf3f6,#e2d2da)" role="img" aria-label="Candelabra"><span>CANDELABRA</span></div>
  <svg class="arrow" style="left:865px" viewBox="0 0 28 36" aria-hidden="true"><path d="M2 2 L22 18 L2 34" fill="none" stroke="var(--pink)" stroke-width="7"/></svg>
  <div class="abs dash" style="left:202px;top:166px;width:658px;border-color:#9fbf56"></div>
  <div class="abs btn-pink" style="left:485px;top:150px">Learn More</div>
</section>

<!-- collections -->
<h2 class="abs heading section-title" style="top:655px">our latest collections</h2>
<svg class="abs" style="left:190px;top:688px;width:682px;height:48px" aria-hidden="true">
  <path d="M12 48 L12 12 L0 28 Z" fill="#dcdcdc"/>
  <path d="M670 48 L670 12 L682 28 Z" fill="#dcdcdc"/>
</svg>
<div class="collection" style="left:202px;background:linear-gradient(180deg,#e6e6e6,#7a7a7a 60%,#c0c0c0)" role="img" aria-label="Long banquet tables with red runners and white chairs"></div>
<div class="collection" style="left:367px;background:linear-gradient(180deg,#f2f0f4,#cfc7d4 50%,#6a6a6a)" role="img" aria-label="White and dark draped backdrop with pink uplighting"></div>
<div class="collection" style="left:534px;background:linear-gradient(180deg,#8a8f7e,#e2e0ee 40%,#c8c0b8)" role="img" aria-label="Reception hall draped in white with lilac lights"></div>
<div class="collection" style="left:699px;background:linear-gradient(180deg,#8a8f7e,#e6e4ef 40%,#c8c0b8)" role="img" aria-label="Reception hall with chandeliers and draped ceiling"></div>
<div class="abs dash" style="left:204px;top:856px;width:654px;border-top-style:dotted;border-color:#f2a8c8"></div>
<div class="abs btn-pink" style="left:485px;top:841px">Take a look</div>

<!-- footer -->
<svg class="abs footer-zig" viewBox="0 0 1062 9" preserveAspectRatio="none" aria-hidden="true">
  <defs><pattern id="zigGrey" width="10" height="9" patternUnits="userSpaceOnUse"><path d="M0 9 L5 0 L10 9 Z" fill="var(--footer)"/></pattern></defs>
  <rect width="1062" height="9" fill="url(#zigGrey)"/>
</svg>
<footer class="abs footer"></footer>

<h3 class="abs heading footer-title" style="left:201px;top:941px">like us</h3>
<div class="abs social-card">
  <div class="abs" style="left:0;top:0;width:35px;height:36px;background:radial-gradient(#f77ab0,#d03a7c)" role="img" aria-label="Lirovel profile flower"></div>
  <div class="abs" style="left:40px;top:2px;font-weight:700;font-size:10px">Lirovel</div>
  <div class="abs" style="left:40px;top:19px;width:32px;height:14px;background:#eee;border:1px solid #ccc;color:#3b5a99;font-size:7px;text-align:center;line-height:12px">Like</div>
  <div class="abs" style="left:0;top:42px;width:147px;border-top:1px solid #a0a0a0"></div>
  <div class="abs" style="left:3px;top:48px;font-size:7.5px">143 people like Lirovel.</div>
  <div class="friend" style="left:3px" role="img" aria-label="Friend avatar"></div>
  <div class="friend" style="left:40px" role="img" aria-label="Friend avatar"></div>
  <div class="friend" style="left:76px" role="img" aria-label="Friend avatar"></div>
  <div class="friend" style="left:112px" role="img" aria-label="Friend avatar"></div>
  <div class="friend-name" style="left:0">Maren</div>
  <div class="friend-name" style="left:37px">Tobias</div>
  <div class="friend-name" style="left:73px">Pippa</div>
  <div class="friend-name" style="left:109px">R.K. Vance</div>
  <div class="abs" style="left:0;top:114px;width:147px;border-top:1px solid #a0a0a0"></div>
  <div class="abs" style="left:3px;top:122px;width:8px;height:8px;background:#3f6fb5"></div>
  <div class="abs" style="left:14px;top:121px;font-size:7.5px">Chatterleaf social plugin</div>
</div>

<h3 class="abs heading footer-title" style="left:377px;top:941px">contact us</h3>
<div class="abs label" style="left:381px;top:979px">Name:</div>
<div class="abs field" style="left:378px;top:997px;width:144px;height:23px"></div>
<div class="abs label" style="left:381px;top:1028px">Number:</div>
<div class="abs field" style="left:378px;top:1046px;width:144px;height:23px"></div>
<div class="abs label" style="left:381px;top:1077px">Email:</div>
<div class="abs field" style="left:378px;top:1095px;width:144px;height:23px"></div>
<div class="abs label" style="left:542px;top:979px">Message:</div>
<div class="abs field" style="left:538px;top:997px;width:164px;height:83px"></div>
<div class="abs send">Send Message</div>

<h3 class="abs heading footer-title" style="left:734px;top:941px">pingvox us</h3>
<div class="abs label" style="left:734px;top:980px;font-size:15px">quick question?</div>
<div class="abs call-box">
  <div class="abs call-btn">Call</div>
  <div class="abs call-icon">
    <svg viewBox="0 0 32 32" width="32" height="32" aria-hidden="true"><path d="M10 7 L14 7 L15 12 L12.5 14 Q15 19 19 21 L21 18.5 L26 19.5 L26 23.5 Q18 25 12 19 Q7 13 10 7 Z" fill="#fff"/></svg>
  </div>
  <div class="abs" style="left:0;width:127px;top:78px;text-align:center;font-family:'Didact Gothic',sans-serif;font-size:20px;color:#7fd0f5">pingvox</div>
</div>

<div class="abs bottom-bar">
  <div class="abs" style="left:203px;top:15px">© Copyright 2013 Lirovel</div>
  <div class="links">Lirovel Brand &nbsp;Collections &nbsp;Features &nbsp;Contact Us</div>
  <div class="icon-square" style="left:811px"></div>
  <div class="icon-square" style="left:836px;background:#22a6e0"></div>
</div>

</body>
</html>
```